New Business Card Design For Re-Branded Company (New Logo)

We recently switched our DBA and had a new logo designed. We now need new business cards made around our new logo. We would like to stick with the color scheme in our logo: White, Orange, and Blue. We want to see original bold designs that reflect our position in the solar energy sector but we prefer simple over complicated.

We are curious about vertical designs so if you can translate your design onto a vertical layout we would be open to look at it. We especially like a few designs we have seen on here that are vertical with a black or very dark gray background. They have our logo on one side and then the normal vertical business card on the other side.

I have included a screenshot of one of the samples we like, labeled sample.jpg and a file we were given as an example of our logo on a dark background.

At the same time we are satisfied to stay with what we have always had in a horizontal format. If it's not a lot of extra work for you, designs that are submitted in both horizontal and vertical formats will be greatly appreciated.

Please submit your original, bold, clean designs for consideration. Contact us with any questions or comments that may arise.

Thank you and Good Luck,

KP

```html
<!DOCTYPE html>
<html lang="en">
<head>
<meta charset="utf-8">
<title>Kestrel Power – Business Card</title>
<link href="https://fonts.googleapis.com/css2?family=Montserrat:wght@600&family=Lato:wght@400&display=swap" rel="stylesheet">
<style>
  :root {
    --backdrop: #cbcbcb;
    --card-dark: #232323;
    --brand-orange: #ee7623;
    --brand-blue: #1b75c9;
    --text-light: #ffffff;
  }
  html, body {
    margin: 0;
    width: 1200px;
    height: 900px;
    overflow: hidden;
    background: var(--backdrop);
  }
  .canvas {
    position: relative;
    width: 1200px;
    height: 900px;
  }
  .card {
    position: absolute;
    top: 184px;
    height: 491px;
  }
  .card--front {
    left: 299px;
    width: 301px;
    background: var(--card-dark);
  }
  .card--back {
    left: 645px;
    width: 305px;
    background: var(--brand-orange);
  }
  .brand-mark {
    position: absolute;
    left: 0;
    right: 0;
    top: 42px;
    text-align: center;
  }
  .brand-mark__dot {
    display: block;
    margin: 0 auto;
    width: 60px;
    height: 60px;
    border-radius: 50%;
    border: 4px solid var(--brand-orange);
    box-sizing: border-box;
  }
  .brand-mark__name {
    display: block;
    margin-top: 16px;
    font-family: "Montserrat", sans-serif;
    font-weight: 600;
    font-size: 27px;
    letter-spacing: -0.2px;
    color: var(--brand-blue);
    white-space: nowrap;
  }
  .contact {
    position: absolute;
    left: 32px;
    top: 297px;
    font-family: "Lato", sans-serif;
    color: var(--text-light);
    font-size: 13px;
    line-height: 18px;
  }
  .contact__name {
    margin: 0;
    font-size: 20px;
    line-height: 24px;
    color: var(--brand-orange);
  }
  .contact__role { margin: 0 0 11px; }
  .contact__address { margin: 0 0 11px; font-style: normal; }
  .contact__list { list-style: none; margin: 0; padding: 0; }
  .contact__list li {
    display: flex;
    align-items: center;
    gap: 8px;
  }
  .contact__list svg { width: 10px; height: 10px; fill: var(--brand-orange); }
  .back-name {
    position: absolute;
    left: 23px;
    bottom: 48px;
    margin: 0;
    font-family: "Montserrat", sans-serif;
    font-weight: 600;
    font-size: 27px;
    letter-spacing: -0.2px;
    color: var(--text-light);
    white-space: nowrap;
  }
</style>
</head>
<body>
<main class="canvas">
  <section class="card card--front">
    <div class="brand-mark">
      <span class="brand-mark__dot"></span>
      <span class="brand-mark__name">KESTREL POWER</span>
    </div>
    <div class="contact">
      <p class="contact__name">Daniel Hart</p>
      <p class="contact__role">Managing Director</p>
      <address class="contact__address">48 Harbour Lane, Suite 12<br>Westbridge, 204816.</address>
      <ul class="contact__list">
        <li>
          <svg viewBox="0 0 10 10" aria-hidden="true"><path d="M2 0.5 L3.6 2.6 L2.8 3.6 C3.4 5 4.9 6.5 6.4 7.2 L7.4 6.4 L9.5 8 L8.6 9.5 C4.5 9.3 0.7 5.5 0.5 1.4 Z"/></svg>
          044-555 010 274
        </li>
        <li>
          <svg viewBox="0 0 10 10" aria-hidden="true"><path d="M0.5 2 H9.5 V8.5 H0.5 Z M1.3 2.6 L5 5.4 L8.7 2.6" stroke="#232323" stroke-width="0.8"/></svg>
          info@kestrelpower.com
        </li>
        <li>
          <svg viewBox="0 0 10 10" aria-hidden="true"><path d="M4.2 5.8 L5.8 4.2 M3.6 4.6 L2 6.2 A1.6 1.6 0 0 0 3.8 8 L5.4 6.4 M6.4 5.4 L8 3.8 A1.6 1.6 0 0 0 6.2 2 L4.6 3.6" fill="none" stroke="#ee7623" stroke-width="1.1" stroke-linecap="round"/></svg>
          www.kestrelpower.com
        </li>
      </ul>
    </div>
  </section>
  <section class="card card--back">
    <p class="back-name">KESTREL POWER</p>
  </section>
</main>
</body>
</html>
```